Brookside Grocer

Hope all is well!

Wanted to make business cards for my father. His name is Faisal Qureshi and owns convenience stores. I have attached logo :)

He does not want any title just simple name and phone. An email would be nice as well.

Faisal Qureshi
Cell: 413-585-2046
Store: 413-719-4820

Brooksidegrocer512@fernpost.com

The design and style is totally up to you :) The colors we were looking for were the same as logo :)

```html
<!DOCTYPE html>
<html lang="en">
<head>
<meta charset="utf-8">
<title>Brookside Grocer – Business Card</title>
<link rel="stylesheet" href="https://fonts.googleapis.com/css2?family=Crimson+Pro:wght@400;700&display=swap">
<style>
  :root {
    --navy: #243775;
    --red: #ee3338;
    --paper: #ffffff;
    --backdrop: #e4e4e4;
    --ink: #3a3a3a;
  }
  * { box-sizing: border-box; margin: 0; padding: 0; }
  html, body {
    width: 1125px;
    height: 1200px;
    overflow: hidden;
    background: var(--backdrop);
  }
  .sheet {
    position: relative;
    width: 1125px;
    height: 1200px;
  }
  .card {
    position: absolute;
    left: 150px;
    width: 825px;
    height: 472px;
    overflow: hidden;
  }
  .card--front { top: 98px; background: var(--paper); }
  .card--back { top: 631px; background: var(--navy); }

  .wordmark {
    position: absolute;
    left: 0;
    width: 100%;
    text-align: center;
    font-family: "Crimson Pro", serif;
    font-weight: 700;
    font-size: 50px;
    letter-spacing: 1px;
    line-height: 1;
  }
  .card--front .wordmark { top: 88px; color: var(--navy); }
  .card--back .wordmark { top: 212px; color: var(--paper); }

  .holder-name {
    position: absolute;
    top: 230px;
    left: 0;
    width: 100%;
    text-align: center;
    font-family: "Crimson Pro", serif;
    font-weight: 700;
    font-size: 34px;
    letter-spacing: 1px;
    color: var(--navy);
  }
  .divider {
    position: absolute;
    top: 295px;
    left: 223px;
    width: 398px;
    height: 1px;
    background: #333;
  }
  .contact-list {
    position: absolute;
    top: 320px;
    left: 0;
    width: 100%;
    list-style: none;
    text-align: center;
    font-family: "Crimson Pro", serif;
    font-size: 22px;
    line-height: 27px;
    color: var(--ink);
  }
  .contact-list li { display: flex; justify-content: center; align-items: center; gap: 7px; }
  .contact-list svg { fill: var(--navy); flex: none; }

  .accent-rule {
    position: absolute;
    left: 0;
    top: 432px;
    width: 100%;
    height: 5px;
    background: var(--red);
  }
  .footer-band {
    position: absolute;
    left: 0;
    top: 437px;
    width: 100%;
    height: 35px;
    background: var(--navy);
  }
</style>
</head>
<body>
<main class="sheet">
  <section class="card card--front">
    <div class="wordmark">BROOKSIDE GROCER</div>
    <h1 class="holder-name">FAISAL QURESHI</h1>
    <div class="divider"></div>
    <ul class="contact-list">
      <li>
        <svg width="16" height="16" viewBox="0 0 24 24" aria-hidden="true"><path d="M6.6 10.8a15.1 15.1 0 0 0 6.6 6.6l2.2-2.2c.3-.3.7-.4 1-.2 1.1.4 2.3.6 3.6.6.6 0 1 .4 1 1V20c0 .6-.4 1-1 1A17 17 0 0 1 3 4c0-.6.4-1 1-1h3.5c.6 0 1 .4 1 1 0 1.3.2 2.5.6 3.6.1.3 0 .7-.2 1z"/></svg>
        <span>413-719-4820</span>
      </li>
      <li>
        <svg width="12" height="19" viewBox="0 0 12 19" aria-hidden="true"><path d="M2 0h8a2 2 0 0 1 2 2v15a2 2 0 0 1-2 2H2a2 2 0 0 1-2-2V2a2 2 0 0 1 2-2zm0 2v13h8V2z"/></svg>
        <span>413-585-2046</span>
      </li>
      <li>
        <svg width="16" height="12" viewBox="0 0 16 12" aria-hidden="true"><path d="M0 0h16v12H0zM1.5 1.5 8 6.5l6.5-5v1.2L8 7.8 1.5 2.7z"/></svg>
        <span>Brooksidegrocer512@fernpost.com</span>
      </li>
    </ul>
    <div class="accent-rule"></div>
    <div class="footer-band"></div>
  </section>

  <section class="card card--back">
    <div class="wordmark">BROOKSIDE GROCER</div>
  </section>
</main>
</body>
</html>
```